Book Cover Project

This is a printed journal front and back cover design. We like the current design, but it feels a little too flat / too simple.

NOTE: we are not looking for a total makeover, just a finishing / polishing of this cover.

Here is our other book cover: https://www.shelvorix.com/Mat-Studio-Blueprint-Calm-Days/dp/7390462815/ref=tmm_hrd_swatch_0?_encoding=UTF8&qid=&sr=
it's purple and yellow (mostly purple)
this one is yellow and we're thinking to add a purple bar at the bottom

Specs: 6 in x 9 in full bleed for print

```html
<!DOCTYPE html>
<html lang="en">
<head>
<meta charset="utf-8">
<title>Quiet Distance Notebook – Cover Spread</title>
<link rel="stylesheet" href="https://fonts.googleapis.com/css2?family=Jost:wght@400;500;600&family=Montserrat:wght@300;400;500;800;900&family=Open+Sans:wght@400&display=swap">
<style>
  :root {
    --backdrop: #9da4e3;
    --yellow-top: #fdda12;
    --yellow-bottom: #f4cd04;
    --purple-band: #4e4f9c;
    --ink: #111111;
    --spine-white: #f7f7f7;
    --name-plate: #f3e48f;
    --photo-light: #d7dbe0;
    --photo-dark: #3d6680;
    --figure-tone: #c99f10;
  }
  * { margin: 0; padding: 0; box-sizing: border-box; }
  html, body {
    width: 1200px; height: 857px; overflow: hidden;
    background: var(--backdrop);
  }
  .spread { position: relative; width: 1200px; height: 857px; }

  .cover {
    position: absolute; top: 150px; width: 370px; height: 555px;
    background: linear-gradient(180deg, var(--yellow-top) 0%, var(--yellow-bottom) 100%);
    overflow: hidden;
    box-shadow: 0 10px 24px rgba(40, 44, 110, 0.28);
  }
  .cover--back { left: 110px; }
  .cover--front { left: 720px; }
  .purple-band {
    position: absolute; left: 0; right: 0; bottom: 0; height: 37px;
    background: var(--purple-band);
  }

  /* Back cover */
  .back-copy {
    position: absolute; left: 30px; width: 312px;
    font-family: "Jost", sans-serif; font-size: 10.6px; line-height: 16.9px;
    color: var(--ink);
  }
  .back-copy p + p { text-indent: 22px; }
  .back-copy strong { font-weight: 600; }
  .blurb { top: 35px; }
  .divider {
    position: absolute; left: 30px; width: 310px; top: 219px;
    border-top: 0.8px solid var(--ink);
  }
  .author-photo {
    position: absolute; left: 30px; top: 241px; width: 77px; height: 108px;
    border-radius: 3px;
    background: linear-gradient(180deg, var(--photo-light) 0%, #b9c2cb 55%, var(--photo-dark) 100%);
  }
  .author-bio { top: 240px; }
  .author-bio .beside-photo { padding-left: 91px; text-indent: 0; }
  .publisher-mark {
    position: absolute; left: 0; right: 0; top: 497px; text-align: center;
    font-family: "Jost", sans-serif; font-weight: 600; font-size: 12px;
    letter-spacing: 2.4px; color: var(--ink);
  }

  /* Spine */
  .spine {
    position: absolute; left: 563px; top: 150px; width: 69px; height: 555px;
    background: var(--spine-white);
    box-shadow: 0 10px 24px rgba(40, 44, 110, 0.28);
  }
  .spine-title {
    position: absolute; left: 50%; top: 62px; transform: translateX(-50%);
    writing-mode: vertical-rl; white-space: nowrap;
    font-family: "Montserrat", sans-serif; font-size: 24px; line-height: 1;
    color: var(--ink);
  }
  .spine-title .w-light { font-weight: 300; letter-spacing: 1px; }
  .spine-title .w-heavy { font-weight: 900; margin-top: 18px; letter-spacing: 1px; }
  .spine-title .w-bold { font-weight: 800; margin-top: 22px; letter-spacing: 1px; }

  /* Front cover */
  .title-line {
    position: absolute; left: 0; right: 0; text-align: center;
    font-family: "Montserrat", sans-serif; color: var(--ink); line-height: 1;
    white-space: nowrap;
  }
  .title-quiet {
    top: 157px; font-weight: 400; font-size: 48px;
    padding-left: 12px;
    display: flex; justify-content: center; align-items: flex-end;
  }
  .runner-figure {
    display: inline-block; width: 16px; height: 66px; margin: 0 6px 3px;
    background: linear-gradient(180deg, #e2b60a 0%, var(--figure-tone) 100%);
    border-radius: 8px;
    opacity: 0.7;
  }
  .title-distance { top: 217px; font-weight: 900; font-size: 44px; padding-left: 14px; letter-spacing: -0.5px; }
  .title-notebook { top: 264px; font-weight: 500; font-size: 44px; padding-left: 10px; }
  .subtitle {
    position: absolute; left: 0; right: 0; top: 310px; text-align: center;
    font-family: "Open Sans", sans-serif; font-size: 13px; color: var(--ink);
    padding-left: 12px;
  }
  .name-plate {
    position: absolute; left: 77px; width: 221px; top: 491px; height: 25px;
    background: var(--name-plate);
    display: flex; align-items: center; justify-content: center;
    font-family: "Montserrat", sans-serif; font-weight: 500; font-size: 12px;
    color: var(--ink);
  }
</style>
</head>
<body>
<main class="spread">

  <section class="cover cover--back" aria-label="Back cover">
    <div class="back-copy blurb">
      <p><strong>PERSONAL TRANSFORMATION</strong> often occurs after failure or pain; but you can also engineer dramatic changes in your life through positive experiences of your own design. Mindfulness is the practice of observing reality as it is, without judgement, and when coupled with running, the experience can be profound.</p>
      <p>The Quiet Distance is an immersive, all-day journey of self-reflection and growth. This notebook is your guidebook as you quiet your mind and move your feet. Whether you are a seasoned runner or have never run further than 5 miles, an equal mix of challenge and reward awaits you. Let’s run, write, and transform.</p>
    </div>

    <div class="divider"></div>

    <div class="author-photo" role="img" aria-label="Portrait photograph of the author"></div>
    <div class="back-copy author-bio">
      <p class="beside-photo"><strong>DANIEL ASHGROVE</strong> is a yoga teacher, trainer, author, podcaster, and entrepreneur. He’s the founder of STRETCHWORKS and the STRETCHWORKS Teachers College and serves as a wellness consultant for companies such as Lumora and Vellify. His growing body of work reaches over 2 million students in 81 countries each month.</p>
      <p>Daniel publishes weekly science-based yoga and lifestyle fitness tutorials via ClipStream, and interviews with leading health and wellness thought leaders via his podcast, The Daniel Ashgrove Show. You can find his published work, event, podcast and teaching schedule at www.StretchWorksStudio.com.</p>
    </div>

    <div class="publisher-mark">STRETCHWORKS</div>
    <div class="purple-band"></div>
  </section>

  <section class="spine" aria-label="Spine">
    <h2 class="spine-title">
      <span class="w-light">QUIET</span><span class="w-heavy">DISTANCE</span><span class="w-bold">NOTEBOOK</span>
    </h2>
  </section>

  <section class="cover cover--front" aria-label="Front cover">
    <h1>
      <span class="title-line title-quiet">QU<span class="runner-figure" role="img" aria-label="Line drawing of a runner standing in for the letter I"></span>ET</span>
      <span class="title-line title-distance">DISTANCE</span>
      <span class="title-line title-notebook">NOTEBOOK</span>
    </h1>
    <p class="subtitle">Run - Write - Transform</p>
    <div class="name-plate">DANIEL ASHGROVE</div>
    <div class="purple-band"></div>
  </section>

</main>
</body>
</html>
```